Tidecrest NZ Brand, Revenue, Promotions & Events

I need an innovative business card that pops my brand. I like the colours against darker gradients and i'm not afraid to be bold.

I run my own Business, Brand, Event & Promotion company. I specialise in breathing life into businesses and adding atmosphere to promotions and events. I am concept based lady that likes to test the boundaries and create stand out campaigns that connect with the consumer.

I have 12 years business experience in a realm of interesting fields form 11 years in coordinating international music festivals & promotions, 6 years in radio with 8 radio awards including a NZ radio award for best sales team in NZ and was the national brand and sales manager for New Zealands 1st indoor entertainment mall. With 10 years of experience in advertising sales, I have an eye for creating revenue streams for businesses and thrive on implementing campaigns that compliment those streams.

I love sayings like "Do what you love, love what you do" and believe that you can achieve anything you want.

I have been fortunate in my career that my connections have carried me without needing to promote my business however it is important that I start to do so.

Target Market(s)

Decision makers 25 to 54

Contact Information for Business Card

Petra Ollingham
Director
p. 022 587 3091
e. petra@tidecrest.nz
www.tidecrest.nz

FB, IG and Linkedin logo

Font styles to use
Sans Serif

Colors

Designer to choose colors to be used in the design.

Requirements
Must have
• Petra Ollingham
• Director
• p. 022 587 3091
• e. petra@tidecrest.nz
• www.tidecrest.nz
• FB, IG and Linkedin logo
Nice to have
• I am looking for a business card with character, that leaves my presence with my customer and makes them remember my brand & optimistic personality when i walk out the door.

```html
<!DOCTYPE html>
<html lang="en">
<head>
<meta charset="utf-8">
<title>Tidecrest NZ — Business Card</title>
<link rel="stylesheet" href="https://fonts.googleapis.com/css2?family=Arimo:wght@400;700&family=Raleway:wght@600;700&display=swap">
<style>
  :root {
    --backdrop: #8a4a20;
    --card-blue: #29a9e1;
    --card-dark: #202020;
    --ink-white: #ffffff;
    --rule-light: rgba(255,255,255,0.75);
    --brand-blue: #29a9e1;
    --tag-grey: #bdbdbd;
    --motto-grey: #c9c9c9;
  }
  * { margin: 0; padding: 0; box-sizing: border-box; }
  html, body { width: 1200px; height: 900px; overflow: hidden; }
  body {
    background: var(--backdrop);
    position: relative;
    font-family: "Arimo", Arial, sans-serif;
  }
  .card { position: absolute; }
  .card-front {
    left: 330px; top: 90px; width: 555px; height: 343px;
    background: var(--card-blue);
    color: var(--ink-white);
    text-align: center;
  }
  .card-back {
    left: 330px; top: 469px; width: 560px; height: 344px;
    background: var(--card-dark);
    text-align: center;
  }
  .holder-name {
    position: absolute; left: 0; right: 0; top: 77px;
    font-family: "Raleway", Arial, sans-serif;
    font-weight: 700; font-size: 20px; letter-spacing: 0.2px;
  }
  .holder-role {
    position: absolute; left: 0; right: 0; top: 100px;
    font-size: 15px;
  }
  .divider-row {
    position: absolute; left: 187px; width: 180px; height: 24px;
    display: flex; align-items: center; justify-content: center; gap: 4px;
  }
  .divider-row::before, .divider-row::after {
    content: ""; flex: 1; height: 1px; background: var(--rule-light);
  }
  .divider-row::before { margin-right: 4px; }
  .divider-row::after { margin-left: 4px; }
  .contact-icons { top: 130px; }
  .social-icons { top: 241px; }
  .icon-tile {
    width: 23px; height: 23px; border-radius: 3px; background: var(--ink-white);
    display: flex; align-items: center; justify-content: center;
  }
  .social-dot {
    width: 23px; height: 23px; border-radius: 50%;
    border: 1.5px solid var(--ink-white);
  }
  .contact-list {
    position: absolute; left: 0; right: 0; top: 164px;
    list-style: none; font-size: 15.5px; line-height: 21.5px;
  }
  .brand-name {
    position: absolute; left: 0; right: 0; top: 140px;
    font-family: "Raleway", Arial, sans-serif;
    font-weight: 600; font-size: 37px; letter-spacing: 2px;
    color: var(--brand-blue);
  }
  .brand-services {
    position: absolute; left: 0; right: 0; top: 186px;
    font-size: 13.5px; color: var(--tag-grey); letter-spacing: 0.2px;
  }
  .brand-motto {
    position: absolute; left: 0; right: 0; top: 288px;
    font-weight: 700; font-size: 16.5px; color: var(--motto-grey);
  }
</style>
</head>
<body>
  <section class="card card-front">
    <h1 class="holder-name">PETRA OLLINGHAM</h1>
    <p class="holder-role">Director</p>
    <div class="divider-row contact-icons">
      <span class="icon-tile" aria-label="Phone">
        <svg width="15" height="13" viewBox="0 0 15 13"><path d="M1 4 Q7.5 -1 14 4 L12 6 L10 4.5 L10 3 Q7.5 2 5 3 L5 4.5 L3 6 Z" fill="#29a9e1"/><rect x="3" y="7" width="9" height="5" rx="1" fill="#29a9e1"/></svg>
      </span>
      <span class="icon-tile" aria-label="Email">
        <svg width="15" height="11" viewBox="0 0 15 11"><rect x="0.5" y="0.5" width="14" height="10" fill="#29a9e1"/><path d="M1 1 L7.5 6.5 L14 1" stroke="#fff" stroke-width="1.2" fill="none"/></svg>
      </span>
      <span class="icon-tile" aria-label="Website">
        <svg width="15" height="15" viewBox="0 0 15 15"><circle cx="7.5" cy="7.5" r="7" fill="#29a9e1"/><ellipse cx="7.5" cy="7.5" rx="3" ry="7" fill="none" stroke="#fff" stroke-width="1"/><line x1="0.5" y1="7.5" x2="14.5" y2="7.5" stroke="#fff" stroke-width="1"/></svg>
      </span>
    </div>
    <ul class="contact-list">
      <li>022 587 3091</li>
      <li>petra@tidecrest.nz</li>
      <li>www.tidecrest.nz</li>
    </ul>
    <div class="divider-row social-icons">
      <span class="social-dot" aria-label="Social profile"></span>
      <span class="social-dot" aria-label="Social profile"></span>
      <span class="social-dot" aria-label="Social profile"></span>
    </div>
  </section>

  <section class="card card-back">
    <h2 class="brand-name">TIDECREST NZ</h2>
    <p class="brand-services">BRAND | REVENUE | EVENTS &amp; PROMOTIONS</p>
    <p class="brand-motto">DO WHAT YOU LOVE, LOVE WHAT YOU DO</p>
  </section>
</body>
</html>
```